Lose Up To 1 LB Of Fat Per Day

We need a double sided street sign for our weight loss clinic. We need the doctors picture to the right side of the sign and we need a challenge “Lose Up To 1 Pound Of Fat Per Day” included in the signage.
Our color scheme for the clinic are black, white, teal and silver.
The phone number should be at the bottom of the sign
517-294–6038

Target Market(s)

Weight Loss

Font styles to use
Sans Serif

```html
<!DOCTYPE html>
<html lang="en">
<head>
<meta charset="utf-8">
<title>Meridian Wellness Clinic – Street Sign</title>
<link rel="stylesheet" href="https://fonts.googleapis.com/css2?family=Poppins:wght@500;600;700;800&display=swap">
<style>
  :root {
    --page: #cccccc;
    --teal-deep: #14918a;
    --teal-light: #37c3b5;
    --charcoal: #2d3b3b;
    --white: #ffffff;
    --photo-tone: #3c5b5a;
  }
  html, body {
    margin: 0;
    width: 1200px;
    height: 1200px;
    overflow: hidden;
    background: var(--page);
  }
  .sign {
    position: absolute;
    left: 90px;
    top: 316px;
    width: 1020px;
    height: 568px;
    font-family: "Poppins", sans-serif;
  }
  .sign svg { display: block; }
  .brand-name { font-family: "Poppins", sans-serif; font-weight: 500; fill: var(--white); letter-spacing: 1.5px; }
  .kicker { font-family: "Poppins", sans-serif; font-weight: 700; fill: var(--white); }
  .headline { font-family: "Poppins", sans-serif; font-weight: 700; fill: var(--white); }
  .per-day { font-family: "Poppins", sans-serif; font-weight: 700; fill: var(--charcoal); }
  .phone { font-family: "Poppins", sans-serif; font-weight: 700; fill: var(--charcoal); }
</style>
</head>
<body>
  <div class="sign">
    <svg width="1020" height="568" viewBox="0 0 1020 568" xmlns="http://www.w3.org/2000/svg">
      <defs>
        <linearGradient id="teal-field" x1="0" y1="0" x2="1" y2="0">
          <stop offset="0" stop-color="var(--teal-deep)"/>
          <stop offset="1" stop-color="var(--teal-light)"/>
        </linearGradient>
        <linearGradient id="photo-fill" x1="0" y1="0" x2="0" y2="1">
          <stop offset="0" stop-color="#8a9c9a"/>
          <stop offset="1" stop-color="var(--photo-tone)"/>
        </linearGradient>
      </defs>

      <rect class="teal-field" x="0" y="0" width="1020" height="402" fill="url(#teal-field)"/>
      <rect class="phone-band" x="0" y="402" width="1020" height="166" fill="var(--white)"/>

      <g class="brand">
        <circle cx="72" cy="88" r="26" fill="none" stroke="var(--white)" stroke-width="3"/>
        <text class="brand-name" x="121" y="88" font-size="27">MERIDIAN</text>
        <text class="brand-name" x="121" y="116" font-size="17">WELLNESS CLINIC</text>
      </g>

      <rect class="doctor-photo" role="img" aria-label="Portrait of the clinic's doctor in a dark suit and purple tie"
            x="52" y="149" width="240" height="253" fill="url(#photo-fill)"/>

      <rect class="kicker-box" x="331" y="46" width="637" height="78" rx="9" fill="var(--charcoal)"/>
      <text class="kicker" x="649" y="109" font-size="64" text-anchor="middle" letter-spacing="5">LOSE UP TO</text>

      <text class="headline" x="339" y="248" font-size="158" textLength="629" lengthAdjust="spacingAndGlyphs">1 POUND</text>
      <text class="headline" x="327" y="372" font-size="150" textLength="486" lengthAdjust="spacingAndGlyphs">OF FAT</text>
      <text class="per-day" x="830" y="315" font-size="58" textLength="111" lengthAdjust="spacingAndGlyphs">PER</text>
      <text class="per-day" x="830" y="369" font-size="58" textLength="132" lengthAdjust="spacingAndGlyphs">DAY</text>

      <text class="phone" x="47" y="530" font-size="135" textLength="917" lengthAdjust="spacingAndGlyphs">517-294–6038</text>
    </svg>
  </div>
</body>
</html>
```